KVRo Business Cards

We need a business card design. We are a Technology (Audio Visual) design, sales and installation company. Looking for a double sided design, clean

Contact Information for Business Card

Clean, modern look, 2 sided

Font styles to use
Sans Serif

```html
<!DOCTYPE html>
<html lang="en">
<head>
<meta charset="utf-8">
<title>KVRo Business Cards</title>
<link rel="stylesheet" href="https://fonts.googleapis.com/css2?family=Arimo:wght@400&display=swap">
<style>
  :root {
    --backdrop: #1d1d1f;
    --card: #2a2a2c;
    --card-back: #111112;
    --gloss: #1a1a1b;
    --accent: #f7941d;
    --text-light: #e6e6e6;
    --text-muted: #a9a9a9;
  }
  * { margin: 0; padding: 0; box-sizing: border-box; }
  html, body { width: 1200px; height: 800px; overflow: hidden; }
  body {
    background: var(--backdrop);
    font-family: "Arimo", Arial, sans-serif;
    font-weight: 400;
    position: relative;
  }
  .card {
    position: absolute;
    top: 250px;
    width: 520px;
    height: 300px;
    border-radius: 3px;
    box-shadow: 0 10px 30px rgba(0,0,0,.5);
    overflow: hidden;
  }
  /* Back side */
  .card-back { left: 60px; background: var(--card-back); }
  .gloss-field {
    position: absolute; inset: 0;
    background: linear-gradient(135deg, var(--gloss), var(--card-back) 60%, var(--gloss));
  }
  .back-wordmark {
    position: absolute;
    left: 0; right: 0; top: 50%;
    transform: translateY(-50%);
    text-align: center;
    font-weight: 400;
    font-size: 28px;
    color: var(--text-light);
  }
  /* Front side */
  .card-front { left: 620px; background: var(--card); color: var(--text-light); }
  .front-wordmark {
    position: absolute;
    left: 140px; top: 52px;
    display: flex; align-items: center; gap: 10px;
    font-weight: 400;
    font-size: 28px;
    color: var(--text-light);
  }
  .wordmark-dot {
    width: 12px; height: 12px;
    background: var(--accent);
  }
  .rule {
    position: absolute;
    height: 2px;
    background: var(--accent);
  }
  .rule-top { left: 300px; top: 102px; width: 205px; }
  .rule-bottom { left: 20px; top: 262px; width: 320px; }
  .holder-name {
    position: absolute;
    left: 140px; top: 108px;
    font-size: 26px;
    font-weight: 400;
    color: var(--accent);
    text-transform: uppercase;
    letter-spacing: .5px;
  }
  .holder-title {
    position: absolute;
    left: 220px; top: 140px;
    font-size: 12px;
    color: var(--text-muted);
    text-transform: uppercase;
    letter-spacing: .5px;
  }
  .contact-row {
    position: absolute;
    left: 150px; top: 170px;
    display: flex; align-items: center; gap: 8px;
    font-size: 13px;
  }
  .divider { width: 1px; height: 16px; background: var(--text-light); margin: 0 6px; }
  .icon { width: 14px; height: 14px; fill: var(--accent); flex: none; }
  .address {
    position: absolute;
    left: 150px; top: 198px;
    display: flex; align-items: flex-start; gap: 8px;
    font-size: 13px; line-height: 17px;
  }
  .website {
    position: absolute;
    left: 222px; top: 238px;
    font-size: 13px;
    color: var(--accent);
  }
</style>
</head>
<body>

  <section class="card card-back" aria-label="Card back">
    <div class="gloss-field" role="img" aria-label="Spot gloss pattern of repeated company names on black"></div>
    <div class="back-wordmark">KVRo</div>
  </section>

  <section class="card card-front" aria-label="Card front">
    <div class="front-wordmark"><span class="wordmark-dot"></span><span>KVRo</span></div>
    <div class="rule rule-top"></div>
    <h1 class="holder-name">Rohan Mehta</h1>
    <p class="holder-title">Managing Director</p>

    <div class="contact-row">
      <span>+91 100 200 3000</span>
      <svg class="icon" viewBox="0 0 16 16" aria-hidden="true"><path d="M4 1h8a1 1 0 0 1 1 1v12a1 1 0 0 1-1 1H4a1 1 0 0 1-1-1V2a1 1 0 0 1 1-1zm1 2v9h6V3zm3 10a.8.8 0 1 0 0 1.6A.8.8 0 0 0 8 13z"/></svg>
      <span class="divider"></span>
      <svg class="icon" viewBox="0 0 16 16" aria-hidden="true"><path d="M1 3h14v10H1zm1.5 1.2L8 8.5l5.5-4.3z"/></svg>
      <span>info@kvro.com</span>
    </div>

    <div class="address">
      <svg class="icon" viewBox="0 0 16 16" aria-hidden="true"><path d="M8 0a5.5 5.5 0 0 0-5.5 5.5C2.5 10 8 16 8 16s5.5-6 5.5-10.5A5.5 5.5 0 0 0 8 0zm0 7.8a2.3 2.3 0 1 1 0-4.6 2.3 2.3 0 0 1 0 4.6z"/></svg>
      <span>Lakeview Road 2nd Block 4th Cross,<br>Sunrise nagar, Bangalore-560000</span>
    </div>

    <div class="website">www.kvro.com</div>
    <div class="rule rule-bottom"></div>
  </section>

</body>
</html>
```